Website wordpress theme for brightvalecrafts.au

We need a modern dark mode website to entice customers to engage us to deliver web apps, mobile apps and VR apps. The site emphasises humans over tech.

Target Market(s)

Medium to large business and well funded startups

Industry/Entity Type

Information Technology

Coding

Coded - Design and coding required

Font styles to use
Sans Serif

Colors
EB3D1F
EC4F4E
F09395
F8D3D4
FCEDEE

Requirements
Must have
• Attractive image on home page

```html
<!DOCTYPE html>
<html lang="en">
<head>
<meta charset="utf-8">
<title>Brightvale Crafts</title>
<link href="https://fonts.googleapis.com/css2?family=Barlow:wght@300;400;500;600;700;800&family=Inter:wght@400;500;600&display=swap" rel="stylesheet">
<style>
:root{
  --bg:#0b1520;
  --panel:#0f1e2d;
  --red:#eb3d1f;
  --red-2:#ec4f4e;
  --pink:#f09395;
  --blush:#f8d3d4;
  --white:#ffffff;
  --muted:#d9dde2;
  --line:#8d96a0;
}
*{margin:0;padding:0;box-sizing:border-box}
html,body{width:1200px;height:3442px;overflow:hidden}
body{
  position:relative;
  background:
    radial-gradient(ellipse 520px 700px at 30% 1600px, rgba(150,40,25,.55), transparent 70%),
    radial-gradient(ellipse 520px 520px at 85% 2150px, rgba(130,35,25,.5), transparent 70%),
    radial-gradient(ellipse 600px 300px at 50% 2330px, rgba(140,35,25,.35), transparent 70%),
    var(--bg);
  color:var(--white);
  font-family:"Inter",sans-serif;
}
.abs{position:absolute}
.btn{
  position:absolute;display:flex;align-items:center;justify-content:center;
  background:linear-gradient(180deg,var(--red-2),var(--red));
  color:#fff;font-family:"Barlow",sans-serif;font-weight:700;font-size:13px;
  border-radius:18px;box-shadow:0 4px 12px rgba(235,61,31,.55);letter-spacing:.2px;
}
.brand{font-family:"Barlow",sans-serif;font-weight:600;color:var(--red);line-height:1;display:flex;align-items:center;gap:8px}
.brand .dot{width:14px;height:14px;border-radius:50%;background:var(--red)}

/* hero */
.hero{position:absolute;left:0;top:0;width:1200px;height:624px;
  background:linear-gradient(100deg,#0c1621 0%,#0f1a25 45%,#5a1a15 75%,#b3301c 100%);overflow:hidden}
.hero-photo{position:absolute;left:560px;top:67px;width:495px;height:557px;
  background:radial-gradient(ellipse at 60% 40%,#d2523a,#7b2418 55%,rgba(60,20,18,0) 80%)}
.nav{position:absolute;left:0;top:0;width:1200px;height:70px}
.nav .brand{position:absolute;left:162px;top:17px;font-size:28px}
.nav ul{position:absolute;left:408px;top:26px;display:flex;gap:0;list-style:none;font-size:11px}
.nav li{margin-right:40px}
.welcome{left:165px;top:172px;font-family:"Barlow",sans-serif;font-size:27px;font-weight:400;letter-spacing:.5px}
.hero-title{left:162px;top:205px;font-family:"Barlow",sans-serif;line-height:.98;font-size:76px}
.hero-title b{font-weight:700;display:block}
.hero-title span{font-weight:300;display:block}
.hero-text{left:162px;top:365px;width:430px;font-size:12.5px;line-height:22px;color:var(--muted)}
.dots{left:165px;top:577px;display:flex;gap:5px}
.dots i{width:5px;height:5px;border-radius:50%;background:#4a5561}
.dots i:first-child{width:9px;height:9px;margin-top:-2px;background:var(--red);box-shadow:0 0 0 2px rgba(235,61,31,.3)}

/* section titles */
.sec-title{position:absolute;left:0;width:1200px;text-align:center;font-family:"Barlow",sans-serif;font-size:33px;font-weight:400}
.sec-title b{font-weight:700;margin-right:8px}
.sec-title::after{content:"";display:block;width:80px;height:3px;background:var(--red);margin:8px auto 0}

/* about */
.about-photo{left:190px;top:684px;width:342px;height:393px;border-radius:8px;
  background:linear-gradient(135deg,#c9b7a0,#8fa5bd 55%,#2e4863)}
.eyebrow{left:600px;top:716px;color:var(--red);font-family:"Barlow",sans-serif;font-size:15px}
.about-title{left:600px;top:736px;font-family:"Barlow",sans-serif;font-size:33px;font-weight:300}
.about-title b{font-weight:700}
.about-rule{left:600px;top:781px;width:80px;height:3px;background:var(--red)}
.about-text{left:600px;top:798px;width:435px;font-size:12.2px;line-height:21.8px;color:var(--muted)}

/* solutions */
.card{position:absolute;top:1230px;width:238px;height:285px;border-radius:12px;background:var(--panel);text-align:center;padding:22px 20px}
.card.active{background:linear-gradient(160deg,#e9451f,#a51d16)}
.card svg{width:58px;height:52px}
.card h3{font-family:"Barlow",sans-serif;font-size:18px;font-weight:400;margin:12px 0 10px}
.card h3 b{font-weight:700}
.card p{font-size:10.6px;line-height:22.4px;color:var(--muted)}

/* how */
.how{left:162px;top:1588px;width:875px;height:268px;border-radius:12px;
  background:linear-gradient(110deg,#6b2219 0%,#3a1c1f 45%,#13202c 100%)}
.how-text{left:222px;top:1695px;width:756px;text-align:center;font-size:11.6px;line-height:22px;color:var(--muted)}
.play{left:571px;top:1827px;width:58px;height:58px;border-radius:50%;background:var(--red);
  box-shadow:0 0 0 4px rgba(235,61,31,.25),0 6px 16px rgba(0,0,0,.5);display:flex;align-items:center;justify-content:center}

/* form */
.field{position:absolute;width:350px;border-bottom:1px solid var(--line);font-size:11.5px;color:var(--muted)}

/* blog */
.post{position:absolute;background:var(--panel)}
.post .img{width:100%}
.post .date{position:absolute;left:18px;background:var(--red);color:#fff;font-family:"Barlow",sans-serif;font-weight:700;font-size:10px;padding:3px 9px}
.post h4{font-family:"Inter",sans-serif;font-weight:700;font-size:13px;line-height:18px;margin:0 17px}
.post p{font-size:9.4px;line-height:14px;color:var(--muted);margin:6px 17px 0}
.post.big h4{font-size:16px;line-height:21px;margin:0 22px}
.post.big p{font-size:10.3px;line-height:16px;margin:8px 22px 0}

/* footer */
.foot-link{position:absolute;font-family:"Barlow",sans-serif;font-size:16px}
.sub-title{left:507px;top:3188px;font-family:"Barlow",sans-serif;font-size:16px}
.sub-input{left:496px;top:3226px;width:245px;height:35px;border-radius:18px;background:#fff;color:#9aa;font-size:9px;padding:13px 30px}
.sub-btn{left:496px;top:3276px;width:245px;height:35px;border-radius:18px;border:1.5px solid var(--red);display:flex;align-items:center;justify-content:center;font-size:11.5px}
.socials{left:866px;top:3284px;display:flex;gap:18px}
.socials i{width:24px;height:24px;border:2.5px solid #fff;border-radius:6px}
.socials i:nth-child(2){border-radius:50%}
.foot-rule{left:156px;top:3360px;width:887px;height:1px;background:#5c6670}
.copy{left:0;top:3392px;width:1200px;text-align:center;font-size:9.6px}
</style>
</head>
<body>

<header class="hero">
  <div class="hero-photo" role="img" aria-label="Two people wearing VR headsets lit in warm red light"></div>
  <nav class="nav">
    <div class="brand"><span class="dot"></span>brightvale crafts</div>
    <ul>
      <li>Home</li><li>About Us</li><li>Our Solutions</li><li>How it Works</li><li>Blog</li><li>Contact Us</li>
    </ul>
    <div class="btn" style="left:922px;top:16px;width:115px;height:35px">GET A QUOTE</div>
  </nav>
  <div class="abs welcome">WELCOME TO</div>
  <h1 class="abs hero-title"><b>Brightvale</b><span>Crafts</span></h1>
  <p class="abs hero-text">Lorem ipsum dolor sit amet, consectetur adipiscing elit, sed do eiusmod tempor incididunt ut labore et dolore magna aliqua.</p>
  <div class="btn" style="left:162px;top:428px;width:114px;height:33px">GET STARTED</div>
  <div class="abs dots"><i></i><i></i><i></i><i></i><i></i></div>
</header>

<section>
  <div class="abs about-photo" role="img" aria-label="Woman in an office chair exploring a VR headset"></div>
  <div class="abs eyebrow">WHO WE ARE</div>
  <h2 class="abs about-title"><b>About Brightvale</b> Crafts</h2>
  <div class="abs about-rule"></div>
  <p class="abs about-text">Lorem ipsum dolor sit amet, consectetur adipiscing elit, sed do eiusmod tempor incididunt ut labore et dolore magna aliqua. iste natus error sit voluptatem accusantium doloremque laudantium, totam rem aperiam, eaque ipsa quae ab illo inventore veritatis et quasi architecto beatae vitae dicta sunt explicabo. Nemo enim ipsam voluptatem quia voluptas sit aspernatur aut odit aut fugit, sed quia consequuntur magni dolores eos qui ratione voluptatem sequi nesciunt. Neque porro quisquam est, qui dolorem ipsum quia dolor sit amet, consectetur, adipisci velit, sed quia non numquam eius modi tempora incidunt ut labore et dolore magnam aliquam quaerat voluptatem.</p>
  <div class="btn" style="left:600px;top:1010px;width:115px;height:33px">LEARN MORE</div>
</section>

<section>
  <h2 class="sec-title" style="top:1145px"><b>Our</b>Solutions</h2>
  <article class="card" style="left:216px">
    <svg viewBox="0 0 58 52" fill="none" stroke="#eb3d1f" stroke-width="2"><rect x="4" y="4" width="30" height="40" rx="3"/><rect x="22" y="12" width="30" height="28" rx="3"/><circle cx="37" cy="26" r="6"/><path d="M34 26l2 2 4-4"/><circle cx="13" cy="14" r="4"/></svg>
    <h3><b>Web</b> Apps</h3>
    <p>Lorem ipsum dolor sit amet, consecte-tur adipiscing elit, sed do eiusmod tempor incididunt ut labore et dolore magna aliqua Quis ipsum suspendisse ultrices gravida Risus commodo viverra maecenas accumsan.</p>
  </article>
  <article class="card active" style="left:481px">
    <svg viewBox="0 0 58 52" fill="none" stroke="#fff" stroke-width="2"><rect x="16" y="2" width="22" height="44" rx="3"/><path d="M22 16l-3 4 3 4M32 16l3 4-3 4M28 14l-2 12"/><circle cx="40" cy="38" r="6"/></svg>
    <h3><b>Mobile</b> Apps</h3>
    <p>Lorem ipsum dolor sit amet, consecte-tur adipiscing elit, sed do eiusmod tempor incididunt ut labore et dolore magna aliqua Quis ipsum suspendisse ultrices gravida Risus commodo viverra maecenas accumsan.</p>
  </article>
  <article class="card" style="left:744px">
    <svg viewBox="0 0 58 52" fill="none" stroke="#eb3d1f" stroke-width="2"><rect x="17" y="4" width="26" height="14" rx="4"/><rect x="6" y="24" width="46" height="18" rx="5"/><path d="M6 30H2v8h4M52 30h4v8h-4M30 18v6"/></svg>
    <h3><b>VR</b> Apps</h3>
    <p>Lorem ipsum dolor sit amet, consecte-tur adipiscing elit, sed do eiusmod tempor incididunt ut labore et dolore magna aliqua Quis ipsum suspendisse ultrices gravida Risus commodo viverra maecenas accumsan.</p>
  </article>
</section>

<section>
  <div class="abs how"></div>
  <h2 class="sec-title" style="top:1631px"><b>How</b>It Works</h2>
  <p class="abs how-text">Lorem ipsum dolor sit amet, consectetur adipiscing elit, sed do eiusmod tempor incididunt ut labore et dolore magna aliqua. iste natus error sit voluptatem accusantium doloremque laudantium, totam rem aperiam, eaque ipsa quae ab illo inventore veritatis et quasi architecto beatae vitae dicta sunt explicabo. Nemo enim ipsam voluptatem quia voluptas sit aspernatur aut odit aut fugit, sed quia consequuntur magni dolores eos qui ratione voluptatem sequi nesciunt. Neque porro quisquam est, qui dolorem ipsum quia dolor sit amet, consectetur, adipisci velit, sed quia non numquam eius modi tempora incidunt.</p>
  <div class="abs play"><svg width="20" height="22" viewBox="0 0 20 22"><path d="M3 1l16 10L3 21z" fill="#fff"/></svg></div>
</section>

<section>
  <h2 class="sec-title" style="top:1933px"><b>Get</b>In Touch</h2>
  <div class="field" style="left:230px;top:2005px;height:48px">First Name *</div>
  <div class="field" style="left:617px;top:2005px;height:48px">Last Name *</div>
  <div class="field" style="left:230px;top:2088px;height:48px">Phone Number *</div>
  <div class="field" style="left:617px;top:2088px;height:48px">Email Address *</div>
  <div class="field" style="left:230px;top:2171px;width:738px;height:71px">Message</div>
  <div class="btn" style="left:542px;top:2278px;width:115px;height:34px">SUBMIT NOW</div>
</section>

<section>
  <h2 class="sec-title" style="top:2385px"><b>Our</b>Latest blog</h2>
  <article class="post big" style="left:131px;top:2473px;width:375px;height:576px">
    <div class="img" style="height:386px;background:linear-gradient(135deg,#0e3a6a,#5aa6dc 50%,#0a2a4e)" role="img" aria-label="Humanoid robot head in blue light"></div>
    <span class="date" style="top:406px">June 24 2023</span>
    <div style="height:44px"></div>
    <h4>Lorem ipsum dolor sit amet, consectetur adipiscing elit sed do eiu.</h4>
    <p>Lorem ipsum dolor sit amet, consectetur adipiscing elit, sed do eiusmod tempor incididunt ut labore et dolore magna aliqua. Ut enim ad minim veniam, quis nostrud exercitation ullamco laboris nisi ut aliquip ex ea commodo consequat.</p>
  </article>
  <article class="post" style="left:524px;top:2473px;width:264px;height:279px">
    <div class="img" style="height:148px;background:linear-gradient(135deg,#2a3f8a,#b04ea0 50%,#1a2a55)" role="img" aria-label="Person at glowing computer screens"></div>
    <span class="date" style="top:138px">June 24 2023</span>
    <div style="height:22px"></div>
    <h4>Lorem ipsum dolor sit amet, conse ctetur adipiscing.</h4>
    <p>Lorem ipsum dolor sit amet, consectetur adipiscing elit, sed do eiusmod tempor incididunt ut labore et dolore magna aliqua. Ut</p>
  </article>
  <article class="post" style="left:806px;top:2473px;width:264px;height:279px">
    <div class="img" style="height:148px;background:linear-gradient(135deg,#1a2a60,#2ec6d8 50%,#6a2a80)" role="img" aria-label="Laptops glowing in neon light"></div>
    <span class="date" style="top:138px">June 24 2023</span>
    <div style="height:22px"></div>
    <h4>Lorem ipsum dolor sit amet, conse ctetur adipiscing.</h4>
    <p>Lorem ipsum dolor sit amet, consectetur adipiscing elit, sed do eiusmod tempor incididunt ut labore et dolore magna aliqua. Ut</p>
  </article>
  <article class="post" style="left:524px;top:2771px;width:264px;height:279px">
    <div class="img" style="height:148px;background:linear-gradient(135deg,#3a3a9a,#7a8ae0 50%,#2a2a6a)" role="img" aria-label="Team working with holographic displays"></div>
    <span class="date" style="top:138px">June 24 2023</span>
    <div style="height:22px"></div>
    <h4>Lorem ipsum dolor sit amet, conse ctetur adipiscing.</h4>
    <p>Lorem ipsum dolor sit amet, consectetur adipiscing elit, sed do eiusmod tempor incididunt ut labore et dolore magna aliqua. Ut</p>
  </article>
  <article class="post" style="left:806px;top:2771px;width:264px;height:279px">
    <div class="img" style="height:148px;background:linear-gradient(135deg,#3a1a5a,#d84a5a 50%,#2a1a4a)" role="img" aria-label="Figure holding a glowing striped sphere"></div>
    <span class="date" style="top:138px">June 24 2023</span>
    <div style="height:22px"></div>
    <h4>Lorem ipsum dolor sit amet, conse ctetur adipiscing.</h4>
    <p>Lorem ipsum dolor sit amet, consectetur adipiscing elit, sed do eiusmod tempor incididunt ut labore et dolore magna aliqua. Ut</p>
  </article>
</section>

<footer>
  <div class="foot-link" style="left:175px;top:3190px">Contact us</div>
  <div class="foot-link" style="left:175px;top:3245px">Imprint</div>
  <div class="foot-link" style="left:175px;top:3299px">Blog</div>
  <div class="foot-link" style="left:325px;top:3190px">Terms of use</div>
  <div class="foot-link" style="left:325px;top:3245px">Privacy Policy</div>
  <div class="foot-link" style="left:325px;top:3299px">Solutions</div>
  <div class="abs sub-title">Subscribe Our Updates and News</div>
  <div class="abs sub-input">Your email</div>
  <div class="abs sub-btn">Subscribe Now</div>
  <div class="abs brand" style="left:822px;top:3198px;font-size:27px"><span class="dot"></span>brightvale crafts</div>
  <div class="foot-link" style="left:866px;top:3257px">Follow us on</div>
  <div class="abs socials" aria-label="Social profiles"><i></i><i></i><i></i></div>
  <div class="abs foot-rule"></div>
  <div class="abs copy">Copyright © 2023 Brightvale Crafts. All Rights Reserved.</div>
</footer>

</body>
</html>
```